Letterhead

We would like to use the logo attached as a new letterhead. Our problem is that we think the dark blue background is too much. We'd like a sleek, professional letterhead, and we'd like at least five options to choose from. I've also uploaded our old letterhead for reference of the style we're going for.

```html
<!DOCTYPE html>
<html lang="en">
<head>
<meta charset="utf-8">
<title>Vale Ridge Strategies Letterhead</title>
<link href="https://fonts.googleapis.com/css2?family=Figtree:wght@400;500;600&display=swap" rel="stylesheet">
<style>
  :root {
    --backdrop: #e0e0e0;
    --paper: #ffffff;
    --navy: #1c2e4a;
    --navy-ink: #0f2a4c;
    --gold: #c6a667;
    --ink: #2b2b2b;
    --muted: #6e6e6e;
  }
  * { margin: 0; padding: 0; box-sizing: border-box; }
  html, body { width: 1200px; height: 1200px; overflow: hidden; }
  body { background: var(--backdrop); font-family: "Figtree", sans-serif; position: relative; }

  .letterhead {
    position: absolute; left: 217px; top: 77px;
    width: 773px; height: 1053px;
    background: var(--paper);
    box-shadow: 4px 6px 14px rgba(0,0,0,0.18);
    overflow: hidden;
  }

  .brand {
    position: absolute; left: 0; right: 0; top: 120px;
    display: flex; justify-content: center; align-items: center; gap: 12px;
  }
  .brand-mark { width: 18px; height: 18px; background: var(--gold); }
  .brand-name {
    font-weight: 600; font-size: 27px; letter-spacing: 2px;
    color: var(--navy); text-transform: uppercase;
  }

  .greeting {
    position: absolute; left: 54px; top: 242px;
    font-size: 23px; font-weight: 600; color: var(--navy-ink);
  }

  .letter-body {
    position: absolute; left: 55px; top: 290px; width: 663px;
    font-size: 17.4px; line-height: 26.2px; color: var(--ink);
    text-align: justify;
  }
  .letter-body p + p { margin-top: 26px; }

  .signatory {
    position: absolute; left: 535px; top: 769px;
    color: var(--muted);
  }
  .signatory-name { font-size: 12px; font-weight: 500; }
  .signatory-title { font-size: 10px; margin-top: 2px; }

  .signature {
    position: absolute; left: 527px; top: 770px; width: 194px; height: 122px;
    background: radial-gradient(ellipse at center, rgba(160,160,160,0.18), rgba(255,255,255,0) 70%);
  }

  .contact {
    position: absolute; left: 57px; top: 945px;
    list-style: none; color: var(--ink); font-size: 22.5px;
  }
  .contact li { display: flex; align-items: center; gap: 8px; height: 31px; }
  .contact svg { width: 24px; height: 22px; fill: var(--gold); }

  .footer-band { position: absolute; left: 0; bottom: 0; width: 773px; height: 48px; }
  .address {
    position: absolute; left: 405px; top: 1018px;
    font-size: 15.6px; color: #ffffff; letter-spacing: -0.2px;
  }
</style>
</head>
<body>
  <main class="letterhead">
    <header class="brand">
      <span class="brand-mark"></span>
      <span class="brand-name">Vale Ridge Strategies</span>
    </header>

    <h1 class="greeting">Dear Mr. John,</h1>

    <section class="letter-body">
      <p>Lorem ipsum dolor sit amet, consectetuer adipiscing elit, sed diam nonummy nibh euismod tincidunt ut laoreet dolore magna aliquam erat volutpat. Ut wisi enim ad minim veniam, quis nostrud exerci tation ullamcorper suscipit lobortis nisl ut aliquip ex ea commodo consequat. Duis autem vel eum iriure dolor in hendrerit in vulputate velit esse molestie consequat, vel illum dolore eu feugiat nulla facilisis at vero eros et accumsan et iusto odio dignissim qui blandit praesent luptatum zzril delenit augue duis dolore te feugait nulla facilisi.</p>
      <p>Lorem ipsum dolor sit amet, cons ectetuer adipiscing elit, sed diam nonummy nibh euismod tincidunt ut laoreet dolore magna aliquam erat volutpat. Ut wisi Lorem ipsum dolor sit amet, consectetuer adipiscing elit, sed diam nonummy nibh euismod tincidunt ut laoreet dolore magna aliquam erat volutpat. Ut wisi enim ad minim veniam, quis nostrud exerci tation ullamcorper suscipit lobortis nisl ut aliquip ex ea commodo consequat. Duis autem vel eum iriure dolor in hendrerit in vulputate velit esse molestie consequat,Lorem ipsum dolor sit amet, cons ectetuer adipiscing elit, sed diam nonummy nibh euismod tincidunt ut laoreet dolore magna aliquam erat volutpat.</p>
    </section>

    <div class="signature" role="img" aria-label="Handwritten signature"></div>
    <div class="signatory">
      <p class="signatory-name">John Doe</p>
      <p class="signatory-title">Office Maneger</p>
    </div>

    <ul class="contact">
      <li>
        <svg viewBox="0 0 24 24" aria-hidden="true"><path d="M6.6 10.8c1.4 2.8 3.8 5.1 6.6 6.6l2.2-2.2c.3-.3.7-.4 1-.2 1.1.4 2.3.6 3.6.6.6 0 1 .4 1 1V20c0 .6-.4 1-1 1C10.6 21 3 13.4 3 4c0-.6.4-1 1-1h3.5c.6 0 1 .4 1 1 0 1.3.2 2.5.6 3.6.1.3 0 .7-.2 1z"/></svg>
        <span>907 555 0142</span>
      </li>
      <li>
        <svg viewBox="0 0 24 20" aria-hidden="true"><path d="M1 3h22v14H1z M3 5l9 7 9-7" fill="none" stroke="#c6a667" stroke-width="2"/><path d="M1 17l8-7M23 17l-8-7" stroke="#c6a667" stroke-width="2"/></svg>
        <span>info@valeridge.com</span>
      </li>
    </ul>

    <svg class="footer-band" viewBox="0 0 773 48" preserveAspectRatio="none" aria-hidden="true">
      <path d="M0 15 H358 C376 15 388 12 398 8 L398 13 C388 17 376 20 358 20 H0 Z" fill="var(--gold)"/>
      <path d="M0 23 H360 C385 23 395 18 410 11 C428 3 440 0 470 0 H773 V48 H0 Z" fill="var(--navy)"/>
    </svg>
    <p class="address">418 K street suite 310 - Anchorage, alaska 99501</p>
  </main>
</body>
</html>
```